BrightVent Coil Services need a Business Card!

Need a business card designed for a new start company called BrightVent! I have attached a Zip file (Please let me know if you cannot open this file) with all logos and also a sheets that includes fonts and colors. Last, you will see the design of our vans which will help design the cards too!
The card is needing to be double sided. A place for email, name, headshot, cell #, Office #, Job Title (Head shot optional)

Target Market(s)

People who need their HVAC filters changed. Residential and Commercial

Industry/Entity Type

Hvac Filter Changing Service

Contact Information for Business Card

Website: brightventcoils.example Office phone: 555.782.3096 The card is needing to be double sided. A place for email, name, headshot, cell #, Office #, Job Title (Head shot optional)

Requirements
Must have
• Color code and fonts form attached sheets and files

```html
<!DOCTYPE html>
<html lang="en">
<head>
<meta charset="utf-8">
<title>BrightVent Business Card</title>
<link href="https://fonts.googleapis.com/css2?family=Montserrat:wght@400;500;600&display=swap" rel="stylesheet">
<style>
  :root {
    --navy: #064b97;
    --sky: #00a8e8;
    --white: #ffffff;
    --backdrop: #e9ecf0;
    --ink-soft: rgba(255,255,255,0.75);
  }
  * { margin: 0; padding: 0; box-sizing: border-box; }
  html, body { width: 1200px; height: 1200px; overflow: hidden; }
  body {
    background: var(--backdrop);
    font-family: "Montserrat", Arial, sans-serif;
    display: flex;
    flex-direction: column;
    align-items: center;
    justify-content: center;
    gap: 60px;
  }
  .card {
    position: relative;
    width: 900px;
    height: 514px;
    border-radius: 40px;
    overflow: hidden;
    box-shadow: 0 10px 30px rgba(0,0,0,0.18);
  }
  .card-bg { position: absolute; inset: 0; width: 100%; height: 100%; }

  .front .brand {
    position: absolute;
    left: 170px;
    top: 120px;
    display: flex;
    align-items: center;
    gap: 22px;
  }
  .brand-mark {
    width: 62px; height: 62px;
    background: var(--sky);
    border-radius: 50%;
  }
  .brand-name {
    font-weight: 600;
    font-size: 88px;
    letter-spacing: -1px;
    line-height: 1;
  }
  .front .brand-name { color: var(--navy); }

  .identity {
    position: absolute;
    left: 140px;
    top: 372px;
    color: var(--white);
  }
  .identity .full-name {
    color: var(--sky);
    font-weight: 500;
    font-size: 34px;
    letter-spacing: 0.5px;
  }
  .identity .position {
    font-weight: 400;
    font-size: 24px;
    letter-spacing: 0.5px;
    margin-top: 2px;
  }
  .divider {
    position: absolute;
    left: 470px;
    top: 330px;
    width: 1px;
    height: 130px;
    background: var(--ink-soft);
  }
  .contacts {
    position: absolute;
    left: 505px;
    top: 330px;
    list-style: none;
    color: var(--white);
    font-size: 22px;
    font-weight: 400;
  }
  .contacts li {
    display: flex;
    align-items: center;
    gap: 12px;
    height: 40px;
  }
  .contacts svg { width: 24px; height: 24px; flex: none; }

  .back { background: var(--navy); }
  .back .brand {
    position: absolute;
    inset: 0;
    display: flex;
    align-items: center;
    justify-content: center;
    gap: 26px;
  }
  .back .brand-name { color: var(--white); font-size: 112px; }
  .back .brand-mark { width: 76px; height: 76px; }
</style>
</head>
<body>

<section class="card front">
  <svg class="card-bg" viewBox="0 0 900 514" preserveAspectRatio="none" aria-hidden="true">
    <rect width="900" height="514" fill="var(--navy)"/>
    <path d="M0 0 H900 V156 C760 316 480 346 0 318 Z" fill="var(--sky)"/>
    <path d="M0 0 H900 V140 C760 300 480 330 0 302 Z" fill="var(--white)"/>
  </svg>

  <div class="brand">
    <span class="brand-mark"></span>
    <span class="brand-name">BrightVent</span>
  </div>

  <div class="identity">
    <div class="full-name">FULL NAME</div>
    <div class="position">POSITION</div>
  </div>

  <div class="divider"></div>

  <ul class="contacts">
    <li>
      <svg viewBox="0 0 24 24"><path fill="var(--sky)" d="M6.6 10.8a15.1 15.1 0 0 0 6.6 6.6l2.2-2.2a1 1 0 0 1 1-.25 11.4 11.4 0 0 0 3.6.57 1 1 0 0 1 1 1V20a1 1 0 0 1-1 1A17 17 0 0 1 3 4a1 1 0 0 1 1-1h3.5a1 1 0 0 1 1 1c0 1.25.2 2.45.57 3.57a1 1 0 0 1-.25 1z"/></svg>
      <span>555.782.3096</span>
    </li>
    <li>
      <svg viewBox="0 0 24 24"><rect x="2" y="5" width="20" height="14" rx="1" fill="var(--sky)"/><path d="M2.5 5.5 L12 13 L21.5 5.5" fill="none" stroke="var(--navy)" stroke-width="1.6"/></svg>
      <span>info@brightventcoils.example</span>
    </li>
    <li>
      <svg viewBox="0 0 24 24" fill="none" stroke="var(--sky)" stroke-width="1.6"><circle cx="12" cy="12" r="9.5"/><ellipse cx="12" cy="12" rx="4" ry="9.5"/><path d="M2.5 12h19M4 7h16M4 17h16"/></svg>
      <span>brightventcoils.example</span>
    </li>
  </ul>
</section>

<section class="card back">
  <div class="brand">
    <span class="brand-mark"></span>
    <span class="brand-name">BrightVent</span>
  </div>
</section>

</body>
</html>
```